Business card design based on existing website

Please make a business card that is consistent with the look and feel of my new website: http://tellbury.com.sg. By going to the site, I think you'll have all you need in terms of the work I do and the colors I use.

I would like to ask the winner of this project to then do a separate project to design my stationery.

Target Market(s)

Heads of human resources, people wanting psychotherapy, and executives wanting coaching. (It's quite a mix!)

Industry/Entity Type

Psychology

Contact Information for Business Card

Email: ray5678@tellbury.com.sg
Website: http://tellbury.com.sg
Tel: +65 94706218

(I will not have a physical address on the card)

Font styles to use
Serif

Colors

Designer to choose colors to be used in the design.

Requirements
Must have
• On the Front
• ==========
• Have "Dr. Raymond Tellbury" using the font of the website.
• Also "Executive Coach, Psychotherapist, Leadership Professor"
• The back should mention
• ==================
• My degrees
• -------------
• "PhD Kelworth; Post Doc Drayfield". E.g., "Raymond Tellbury (PhD Kelworth; Post Doc Drayfield)" where the text between brackets was in smaller font.
• My work
• ----------
• "Executive coach, psychotherapist, and leadership professor"
• My job titles
• ---------------
• "Principal (Tellbury Consulting)
• Adjunct Professor (Lornvale Commerce University)
• Adjunct Associate Professor (Pemberly Institute of Letters)
• Coach & Supervisor (OKTRAV) '
• Options:
• 1) you can abbreviate Adjunct Professor to "Adj Prof" or "Adj Professor"; and "Adjunct Associate Professor" to "Adj Assoc Prof"
• 2) you abbreviate "Pemberly Institute of Letters" and "Lornvale Commerce University" to "PIL" and "LCU"
• 3) You can also combine the titles for PIL and LCU, e.g., "Adjunct faculty (PIL & LCU)
Nice to have
• Because I work with many Chinese people, it is sometimes helpful to have my family name, "Tellbury", in caps. In the past I have not used caps because it takes away from the aesthetic of the card. Only use caps if it looks good.
• The uploaded image of a "RT" is something that may be helpful. I am undecided.
• THANK YOU for helping me!
Should not have
• No photos. In my industry people consider it overselling.

```html
<!DOCTYPE html>
<html lang="en">
<head>
<meta charset="utf-8">
<title>Raymond Tellbury – Business Card</title>
<link rel="stylesheet" href="https://fonts.googleapis.com/css2?family=Crimson+Text:wght@400;600;700&display=swap">
<style>
  :root {
    --backdrop: #e2e2e2;
    --green-deep: #1a2a1c;
    --green-mid: #14482a;
    --green-bright: #0b8a3d;
    --ink-light: #f4f6f2;
    --paper: #f1f1f0;
    --ink-dark: #1d2b1d;
    --ink-muted: #5a5a5a;
  }
  * { box-sizing: border-box; margin: 0; padding: 0; }
  html, body {
    width: 1200px;
    height: 960px;
    overflow: hidden;
    background: var(--backdrop);
    font-family: "Crimson Text", Georgia, serif;
  }
  .card {
    position: absolute;
    width: 600px;
    height: 343px;
    box-shadow: 1px 2px 3px rgba(0,0,0,0.35);
    overflow: hidden;
  }
  .card-front { left: 314px; top: 113px; color: var(--ink-light); }
  .card-back { left: 311px; top: 472px; background: var(--paper); }

  .front-bg { position: absolute; inset: 0; width: 100%; height: 100%; }

  .contact-list {
    position: absolute;
    right: 33px;
    top: 42px;
    list-style: none;
    text-align: right;
    font-size: 13px;
    line-height: 19.5px;
  }
  .contact-list li { display: flex; justify-content: flex-end; align-items: center; gap: 8px; }
  .contact-icon { width: 13px; height: 13px; fill: var(--ink-light); }

  .identity { position: absolute; left: 40px; top: 164px; }
  .person-name { font-size: 30px; font-weight: 700; line-height: 34px; letter-spacing: -0.2px; }
  .degrees { font-size: 14px; font-weight: 700; line-height: 18px; margin-top: 0; }
  .roles { font-size: 14.5px; line-height: 19px; margin-top: 11px; }

  .back-name {
    position: absolute;
    left: 0; right: 0;
    top: 138px;
    text-align: center;
    font-size: 45px;
    font-weight: 700;
    color: var(--ink-dark);
    letter-spacing: -0.5px;
  }
  .back-web {
    position: absolute;
    left: 0; right: 0;
    top: 298px;
    text-align: center;
    font-size: 12px;
    letter-spacing: 4.2px;
    color: var(--ink-muted);
  }
</style>
</head>
<body>
  <section class="card card-front" aria-label="Card front">
    <svg class="front-bg" viewBox="0 0 600 343" preserveAspectRatio="none" aria-hidden="true">
      <defs>
        <linearGradient id="baseGreen" x1="0" y1="0" x2="1" y2="0.35">
          <stop offset="0" stop-color="var(--green-deep)"/>
          <stop offset="0.55" stop-color="var(--green-mid)"/>
          <stop offset="1" stop-color="var(--green-bright)"/>
        </linearGradient>
        <linearGradient id="sheen" x1="0" y1="0" x2="1" y2="0.6">
          <stop offset="0" stop-color="#ffffff" stop-opacity="0.55"/>
          <stop offset="0.55" stop-color="#ffffff" stop-opacity="0.25"/>
          <stop offset="1" stop-color="#ffffff" stop-opacity="0"/>
        </linearGradient>
      </defs>
      <rect width="600" height="343" fill="url(#baseGreen)"/>
      <polygon points="123,0 600,0 600,288" fill="url(#sheen)"/>
    </svg>

    <ul class="contact-list">
      <li>+65 94706218
        <svg class="contact-icon" viewBox="0 0 16 16" aria-hidden="true"><path d="M3.6 1.2l2.3 2.6-1.3 2a9 9 0 0 0 5.6 5.6l2-1.3 2.6 2.3-1.4 2.2C7.6 16 0 8.4 1.4 2.6z"/></svg>
      </li>
      <li>ray5678@tellbury.com.sg
        <svg class="contact-icon" viewBox="0 0 16 16" aria-hidden="true"><path d="M1 3h14v10H1z M2.2 4.2v.4L8 8.8l5.8-4.2v-.4z" fill-rule="evenodd"/></svg>
      </li>
      <li>tellbury.com.sg
        <svg class="contact-icon" viewBox="0 0 16 16" aria-hidden="true"><circle cx="8" cy="8" r="7"/><path d="M4 4.5c2 .3 2.5 1.8 1.8 3.2-.6 1.2.5 2.6 1.8 3 .8.3.5 2 0 3.2M10.5 2.6c-.6 1.4.2 2.4 1.6 2.6 1 .1 1.8 1 1.6 2.2" stroke="#14482a" stroke-width="1.4" fill="none"/></svg>
      </li>
    </ul>

    <div class="identity">
      <h1 class="person-name">Raymond Tellbury</h1>
      <p class="degrees">(PhD Kelworth; Post Doc Drayfield)</p>
      <p class="roles">
        Executive coach, psychotherapist, and<br>
        leadership trainer Principal (Tellbury Consulting)<br>
        Adj Prof (LCU) Adj Assoc Prof(PIL)<br>
        Coach &amp; Supervisor (OKTRAV)
      </p>
    </div>
  </section>

  <section class="card card-back" aria-label="Card back">
    <h2 class="back-name">Raymond Tellbury</h2>
    <p class="back-web">www.tellbury.com.sg</p>
  </section>
</body>
</html>
```